Retail Seafood business needs package/label design

In need of packaging/label design for multiple seafood products such as sword fish, halibut, cod fish, scallops, mahi, catfish, and lobster tails

```html
<!DOCTYPE html>
<html lang="en">
<head>
<meta charset="utf-8">
<title>Seafood Label Dieline</title>
<link href="https://fonts.googleapis.com/css2?family=Poiret+One&family=Poppins:ital,wght@1,800&display=swap" rel="stylesheet">
<style>
  :root {
    --backdrop: #07000f;
    --panel: #3c3640;
    --panel-edge: #8a808f;
    --label-dark: #1f1b22;
    --label-frame: #4a4350;
    --light-block: #e3d3e6;
    --copy: #d8cad8;
    --muted: #615866;
  }
  html, body { margin: 0; padding: 0; overflow: hidden; }
  body { width: 1200px; height: 1200px; background: var(--backdrop); position: relative; }
  .dieline { position: absolute; left: 0; top: 0; width: 1200px; height: 1200px; }
  .body-copy {
    position: absolute; left: 178px; top: 514px; width: 200px;
    font-family: "Poiret One", sans-serif; font-size: 12.4px; line-height: 19.4px;
    color: var(--copy); text-align: center; margin: 0;
  }
  .side-box {
    position: absolute; left: 851px; top: 548px; width: 143px; height: 218px;
    border: 1px solid #5e5664; border-radius: 3px; box-sizing: border-box;
  }
  .side-copy {
    margin: 28px 8px 0; font-family: "Poiret One", sans-serif; font-size: 9.6px;
    line-height: 15.2px; color: var(--copy); text-align: center;
  }
  .brand-mark {
    position: absolute; left: 528px; top: 460px; width: 150px; text-align: center;
    font-family: "Poppins", sans-serif; font-style: italic; font-weight: 800;
    font-size: 26px; color: #9c8fa0; letter-spacing: 1px;
  }
  .product-name {
    position: absolute; left: 480px; top: 502px; width: 246px; text-align: center;
    font-family: "Poiret One", sans-serif; font-size: 66px; line-height: 66px;
    color: transparent; -webkit-text-stroke: 1.2px #9c8fa0;
  }
  .tagline {
    position: absolute; left: 480px; top: 571px; width: 246px; text-align: center;
    font-family: "Poppins", sans-serif; font-style: italic; font-weight: 800;
    font-size: 21px; color: var(--muted);
  }
</style>
</head>
<body>
<svg class="dieline" viewBox="0 0 1200 1200" xmlns="http://www.w3.org/2000/svg">
  <g class="panel-edges" fill="none" stroke="var(--panel-edge)" stroke-width="2">
    <rect x="168" y="503" width="864" height="291" rx="6"/>
    <rect x="396" y="456" width="408" height="384" rx="36"/>
    <rect x="458" y="421" width="284" height="453" rx="36"/>
  </g>
  <g class="panel-fill" fill="var(--panel)" role="img" aria-label="Line-drawn seafood pattern of crabs, lobsters, fish, sushi, herbs and lemon slices">
    <rect x="169" y="504" width="862" height="289" rx="5"/>
    <rect x="397" y="457" width="406" height="382" rx="35"/>
    <rect x="459" y="422" width="282" height="451" rx="35"/>
  </g>
  <g class="fold-lines" stroke="var(--panel-edge)" stroke-width="1" fill="var(--panel)">
    <line x1="396" y1="514" x2="396" y2="787"/>
    <line x1="804" y1="514" x2="804" y2="787"/>
    <rect x="387" y="642" width="18" height="18" transform="rotate(45 396 651)"/>
    <rect x="795" y="642" width="18" height="18" transform="rotate(45 804 651)"/>
  </g>
  <path class="front-label" fill="var(--label-dark)"
        d="M479 514 H492 Q500 500 505 480 Q520 440 603 438 Q686 440 701 480 Q706 500 714 514 H727 V803 H714 Q705 830 690 835 H516 Q501 830 492 803 H479 Z"/>
  <path class="front-label-frame" fill="none" stroke="var(--label-frame)" stroke-width="1"
        d="M490 488 H716 Q716 515 728 518 V795 Q716 800 716 824 H490 Q490 800 478 795 V518 Q490 515 490 488 Z" transform="translate(0 0)"/>
  <ellipse class="logo-plate" cx="603" cy="477" rx="75" ry="30" fill="var(--light-block)"/>
  <g class="rating-stars" fill="#4c4551">
    <polygon points="544,624 546,629 551,629 547,632 548,637 544,634 540,637 541,632 537,629 542,629"/>
    <polygon points="572,611 574.5,617 581,617 576,621 578,627 572,623 566,627 568,621 563,617 569.5,617"/>
    <polygon points="604,606 607,613 614,613 608.5,617.5 610.5,624 604,620 597.5,624 599.5,617.5 594,613 601,613"/>
    <polygon points="636,611 638.5,617 645,617 640,621 642,627 636,623 630,627 632,621 627,617 633.5,617"/>
    <polygon points="663,624 665,629 670,629 666,632 667,637 663,634 659,637 660,632 656,629 661,629"/>
  </g>
  <rect class="info-block" x="490" y="661" width="227" height="106" fill="var(--light-block)"/>
  <rect class="leaf-icons" x="891" y="717" width="66" height="36" rx="6" fill="#5a5260" role="img" aria-label="Three small leaf icons"/>
</svg>

<div class="brand-mark">LOGO</div>
<div class="product-name">Name</div>
<div class="tagline">Tagline</div>

<p class="body-copy">Lorem ipsum dolor sit amet consectetuer adipiscing elit sed diam nonummy nibh euismod tincidunt ut laoreet dolore magna aliquam erat volutpat Ut wisi enim ad minim veniam quis nostrud exerci tation ullamcorper suscipit lobortis nisl ut aliquip ex ea commodo consequat Duis autem vel eum iriure dolor in hendrerit in vulputate velit esse molestie consequat vel illum dolore eu feugiat nulla facilisis at vero eros et accumsan et iusto odio dignissim qui blandit praesent luptatum zzril delenit augue</p>

<div class="side-box">
  <p class="side-copy">Lorem Ipsum Dolor Sit Amet, Consectetur Adipiscing Elit, Sed Do Eiusmod Tempor Incididunt Ut Labore Et Dolore Magna Aliqua. Ut Enim Ad Minim Veniam, Quis Nostrud Exercitation Ullamco Laboris Nisi Ut Aliquip Ex Ea Commodo Consequat.</p>
</div>
</body>
</html>
```